ASL Learning Website Application Pages Redesign

Introduction:
We need a redesign of the internal pages of our website, SignQuiverly.com. The current website design has been in place for many years and is not mobile friendly. We want an updated design that makes the site look cleaner, more professional, and mobile accessible. We are looking for a design that eliminates the clutter on each page, and makes the site simple and easy to use. We will be interested in your design if it is unique and creative. Don't be afraid to completely change the look of the site.

We need the designs sliced up into clean HTML files that are responsive and work well on both mobile and desktop computers. We will implement the PHP needed to make the pages functional.

About Us:
SignQuiverly is a subscription-based website for American Sign Language (ASL) video lessons. The content is for anyone who wishes to learn ASL, regardless of age. It has been designed to instruct Deaf students, parents of Deaf children, and the community-at-large. All lessons are taught by Deaf experts of ASL.

Overview:
The website before log-in does not need any changes. There are five key pages within the internal website (after log-in) that need to be redesigned; they are listed below. Note that some pages (Dictionary and Activity) have multiple sub-pages, so there are about 6-8 pages in total to design, depending on how you decide to approach this (more info in the pages’ respective instruction documents).

The new page designs should retain their existing features, and as stated before, should be mobile friendly. However, you may combine, collapse, or completely change the look of these features. Each page to redesign has a separate instruction document attachment, and screenshots of the current version of the page. Our logo has also been attached. If you want to see the website pages for yourself, you can also go to our website (SignQuiverly.com) and use a free trial to get access to the internal site.

As for design preferences, we want our site to be modern-looking and mature. We’re looking for an inviting, educational style that can attract both high school students and adults. We’re happy with the current font and color scheme, but we’re always open to ideas!

Additional Notes:
- Every page has the same header and footer. You could keep these the same, or change them, based on your discretion.
- Currently, every page also has a breadcrumb. The breadcrumb is unnecessary and you may remove it. However, the “add/remove from favorites” button on the right of the breadcrumb is necessary to keep somewhere on the page.

Pages:
Here’s a list of the five key pages we need redesigned:
- Dashboard
- Dictionary
- Lesson
- Activity
- All Lessons

Each page has its own instruction document. These are attached separately.

Just purchased a $150 for Top designers. I need to give them time to submit their designs . Can I have 7 more days?

Target Market(s)

Deaf students, parents of Deaf children, and the community-at-large interested in learning ASL

Coding

Number of Pages Required

5+ page

Font styles to use
Sans Serif

Requirements
Must have
• Responsive design - the full application experience should be available on mobile devices.
Follow the directions on the design brief.
Nice to have
• Be creative! Please play around with, or even completely change, the look of the site.

```html
<!DOCTYPE html>
<html lang="en">
<head>
<meta charset="utf-8">
<title>SignQuiverly – Activity Pages</title>
<link href="https://fonts.googleapis.com/css2?family=Lato:ital,wght@0,400;0,700;0,900;1,400;1,700&display=swap" rel="stylesheet">
<style>
:root{
  --stage:#7b8a90;
  --green:#4f9b2b;
  --green-text:#4a9a22;
  --cream:#fbefdc;
  --orange:#f07a14;
  --panel:#f3f3f3;
  --ink:#222;
  --muted:#666;
  --line:#dcdcdc;
  --white:#fff;
  --video-a:#6fb88a;
  --video-b:#3e8a60;
}
*{box-sizing:border-box;margin:0;padding:0}
html,body{width:1200px;height:924px;overflow:hidden}
body{background:var(--stage);font-family:'Lato',Arial,sans-serif;color:var(--ink);position:relative}
.page{position:absolute;top:37px;width:619px;height:1552px;background:var(--white);transform:scale(0.5495);transform-origin:0 0;overflow:hidden}
.page--one{left:34px}.page--two{left:422px}.page--three{left:810px}
.abs{position:absolute}

/* header */
.site-header{position:absolute;left:0;top:0;width:619px;height:68px;background:var(--green)}
.brand-box{position:absolute;left:0;top:0;width:241px;height:68px;background:var(--cream);display:flex;align-items:center;justify-content:center;gap:8px}
.brand-box::after{content:"";position:absolute;right:-8px;top:26px;border-left:8px solid var(--cream);border-top:8px solid transparent;border-bottom:8px solid transparent}
.brand-dot{width:14px;height:14px;border-radius:50%;background:var(--green)}
.brand-name{font-size:22px;font-weight:700;color:var(--green)}
.header-title{position:absolute;left:271px;top:18px;color:#fff;font-weight:900;font-size:11px;letter-spacing:-.2px}
.header-user{position:absolute;left:271px;top:40px;color:#e6f3dc;font-size:8px}
.main-nav{position:absolute;left:0;top:68px;width:619px;height:27px;background:var(--orange);display:flex;align-items:center;padding-left:42px;gap:14px}
.main-nav span{color:#fff;font-size:7px;font-weight:700}

/* activity bar */
.activity-bar{position:absolute;left:0;top:95px;width:619px;height:70px;border-bottom:1px solid var(--line)}
.activity-title{position:absolute;left:39px;top:19px;font-size:11px;font-weight:700}
.activity-title em{font-style:normal;color:var(--green-text)}
.activity-sub{position:absolute;left:39px;top:40px;font-size:8px;font-style:italic;color:#444}
.fav-label{position:absolute;left:473px;top:31px;font-size:7px;font-weight:700}
.fav-btn{position:absolute;left:540px;top:27px;width:41px;height:19px;border:1px solid var(--line);background:#fafafa;font-size:9px;font-weight:700;text-align:center;line-height:17px}
.fav-btn b{color:var(--green-text)}

.section-title{position:absolute;left:38px;top:186px;font-size:14px;font-style:italic;font-weight:700;color:var(--green-text)}

/* question cards */
.card{position:absolute;left:38px;width:543px;height:182px;background:var(--panel)}
.badge{position:absolute;left:-7px;top:6px;width:37px;height:30px;background:var(--orange);color:#fff;font-size:15px;font-weight:700;padding:4px 0 0 12px}
.badge::after{content:"";position:absolute;left:0;bottom:-7px;border-top:7px solid #b9580a;border-left:7px solid transparent}
.options{position:absolute;left:11px;top:48px;list-style:none}
.options li{height:27.2px;font-size:8px;display:flex;align-items:center;gap:10px;font-weight:700;color:#333}
.box{width:8px;height:8px;border:1.2px solid #333;flex:none}
.answer{position:absolute;right:233px;top:158px;font-size:8px;font-weight:700}
.answer span{color:var(--green-text)}
.reviewed{position:absolute;left:11px;top:163px;font-size:7px;font-weight:700;display:flex;align-items:center;gap:10px}

.video{position:absolute;background:radial-gradient(ellipse at 50% 55%,var(--video-a),var(--video-b));border-radius:4px;overflow:hidden}
.video--wide{left:299px;top:15px;width:230px;height:150px}
.video--half{top:13px;width:218px;height:142px}
.video--a{left:50px}.video--b{left:312px}
.video .slow{position:absolute;left:3px;top:3px;background:rgba(0,0,0,.25);color:#eee;font-size:6px;padding:1px 4px;border-radius:2px}
.video .play{position:absolute;left:50%;top:50%;width:34px;height:34px;margin:-17px 0 0 -17px}
.video .controls{position:absolute;left:0;bottom:0;width:100%;height:22px;background:linear-gradient(transparent,rgba(0,0,0,.7));color:#fff;font-size:6px;padding:6px 8px 0}
.video .controls i{position:absolute;left:8px;right:60px;bottom:4px;height:1.5px;background:rgba(255,255,255,.5)}
.video .controls em{position:absolute;right:8px;top:6px;font-style:normal;letter-spacing:6px}

.submit{position:absolute;left:222px;top:1214px;width:176px;height:29px;border-radius:15px;background:var(--green);color:#fff;font-size:8px;font-weight:900;text-align:center;line-height:29px}

/* footer */
.site-footer{position:absolute;left:0;top:1278px;width:619px;height:274px;background:var(--panel)}
.foot-brand{position:absolute;left:36px;top:38px;display:flex;align-items:center;gap:6px}
.foot-brand .brand-name{font-size:19px}
.foot-brand .brand-dot{width:11px;height:11px}
.foot-about{position:absolute;left:36px;top:82px;width:160px;font-size:6.3px;line-height:13.7px;color:#555}
.foot-col{position:absolute;top:30px;font-size:6.3px;color:#555;line-height:13.8px}
.foot-col h4{font-size:10px;color:var(--ink);margin-bottom:4px}
.quick{left:223px}.quick2{left:316px;top:50px}
.contact{left:429px}
.contact p{display:flex;align-items:center;gap:6px;margin-bottom:7px}
.rule-v{position:absolute;top:30px;width:1px;height:150px;background:var(--line)}
.rule-h{position:absolute;left:36px;top:212px;width:550px;height:1px;background:var(--line)}
.copy{position:absolute;left:36px;top:226px;font-size:6.3px;color:#555;line-height:13.5px}
.socials{position:absolute;left:463px;top:223px;display:flex;gap:7px}
.socials span{width:18px;height:18px;border-radius:50%;border:1px solid #9ccf85;background:#fff}
.badge-box{position:absolute;left:587px;top:222px;width:32px;height:30px;background:#e4e4e4;border:1px solid #ccc}
.x10{position:absolute;left:600px;top:258px;font-size:6.5px;color:#3a7bd5}
</style>
</head>
<body>

<!-- reusable play icon -->
<svg width="0" height="0" style="position:absolute">
  <defs>
    <symbol id="play" viewBox="0 0 34 34"><circle cx="17" cy="17" r="16" fill="#fff"/><path d="M13 10 L25 17 L13 24 Z" fill="#f07a14"/></symbol>
    <symbol id="pin" viewBox="0 0 10 10"><path d="M5 0C2.8 0 1.5 1.6 1.5 3.5 1.5 6 5 10 5 10S8.5 6 8.5 3.5C8.5 1.6 7.2 0 5 0Z" fill="#4f9b2b"/><circle cx="5" cy="3.6" r="1.3" fill="#fff"/></symbol>
    <symbol id="phone" viewBox="0 0 10 10"><path d="M2 0.8 3.8 3 2.9 4.2C3.6 5.7 4.4 6.5 5.8 7.1L7 6.2 9.2 8 8 9.6C4.2 9.3 0.7 5.8 0.4 2Z" fill="#4f9b2b"/></symbol>
    <symbol id="mail" viewBox="0 0 10 10"><rect x="0.5" y="2" width="9" height="6.5" fill="#4f9b2b"/><path d="M0.5 2 5 5.5 9.5 2" stroke="#fff" stroke-width="0.8" fill="none"/></symbol>
  </defs>
</svg>

<!-- PAGE 1 -->
<section class="page page--one">
  <header class="site-header">
    <div class="brand-box"><span class="brand-dot"></span><span class="brand-name">SignQuiverly</span></div>
    <div class="header-title">HOW TO LEARN ASL THROUGH VIDEO LESSONS ONLINE</div>
    <div class="header-user">You are currently logged in as &nbsp;Mlarkin</div>
  </header>
  <nav class="main-nav"><span>DASHBOARD</span><span>LESSONS</span><span>LESSONS LIST</span><span>DICTIONARY</span><span>HANDSHAPES</span><span>LOCATIONS</span><span>DICTIONARY</span><span>UPDATE ACCOUNTS</span><span>LOG OUT</span></nav>
  <div class="activity-bar">
    <div class="activity-title"><em>Activity:</em> Choose the Correct Sentence</div>
    <div class="activity-sub">After viewing the video choose the correct word &amp; phrase</div>
    <div class="fav-label">Add to Favorites</div>
    <div class="fav-btn"><b>+</b> / -</div>
  </div>
  <h2 class="section-title">Choose the Correct Sentence</h2>

  <article class="card" style="top:216px"><div class="badge">1</div>
    <ul class="options"><li><span class="box"></span>Blue cars are my favorite</li><li><span class="box"></span>I love yellow cars</li><li><span class="box"></span>Did you see the silver car?</li><li><span class="box"></span>I want a yellow car.</li></ul>
    <div class="video video--wide" role="img" aria-label="ASL instructor signing the sentence on a green backdrop"><span class="slow">Slow video playback</span><svg class="play"><use href="#play"/></svg><div class="controls">▶ &nbsp;0:00 / 0:04<em>◀ ⛶ ⋮</em><i></i></div></div>
  </article>
  <article class="card" style="top:413px"><div class="badge">2</div>
    <ul class="options"><li><span class="box"></span>Pink is a nice color.</li><li><span class="box"></span>Purple is a nice color.</li><li><span class="box"></span>Green and white are the best colors.</li><li><span class="box"></span>love the color orange.</li></ul>
    <div class="video video--wide" role="img" aria-label="ASL instructor signing the sentence on a green backdrop"><span class="slow">Slow video playback</span><svg class="play"><use href="#play"/></svg><div class="controls">▶ &nbsp;0:00 / 0:04<em>◀ ⛶ ⋮</em><i></i></div></div>
  </article>
  <article class="card" style="top:609px"><div class="badge">3</div>
    <ul class="options"><li><span class="box"></span>I love blue and yellow!</li><li><span class="box"></span>I love scarlet and grey.</li><li><span class="box"></span>I love green and white.</li><li><span class="box"></span>I like blue and yellow!</li></ul>
    <div class="video video--wide" role="img" aria-label="ASL instructor signing the sentence on a green backdrop"><span class="slow">Slow video playback</span><svg class="play"><use href="#play"/></svg><div class="controls">▶ &nbsp;0:00 / 0:04<em>◀ ⛶ ⋮</em><i></i></div></div>
  </article>
  <article class="card" style="top:806px"><div class="badge">4</div>
    <ul class="options"><li><span class="box"></span>Blue and yellow make green.</li><li><span class="box"></span>My favorite colors are red and white.</li><li><span class="box"></span>Do you like white and tan.</li><li><span class="box"></span>Her shirt is rad and purple.</li></ul>
    <div class="video video--wide" role="img" aria-label="ASL instructor signing the sentence on a green backdrop"><span class="slow">Slow video playback</span><svg class="play"><use href="#play"/></svg><div class="controls">▶ &nbsp;0:00 / 0:04<em>◀ ⛶ ⋮</em><i></i></div></div>
  </article>
  <article class="card" style="top:1003px"><div class="badge">5</div>
    <ul class="options"><li><span class="box"></span>Doyou like the color green?</li><li><span class="box"></span>Do You like orange or yellow?</li><li><span class="box"></span>I don't like the color orange.</li><li><span class="box"></span>Do you like the color orange?</li></ul>
    <div class="video video--wide" role="img" aria-label="ASL instructor signing the sentence on a green backdrop"><span class="slow">Slow video playback</span><svg class="play"><use href="#play"/></svg><div class="controls">▶ &nbsp;0:00 / 0:04<em>◀ ⛶ ⋮</em><i></i></div></div>
  </article>

  <div class="submit">I.M' DONE SUBMIT MY ANSWERS</div>

  <footer class="site-footer">
    <div class="foot-brand"><span class="brand-dot"></span><span class="brand-name">SignQuiverly</span></div>
    <p class="foot-about">SignQuiverly is a subscription based website for American Sign Language (ASL) video lessons. The content is for anyone who wishes to learn ASL, regardless of age. It has been designed to instruct Deaf students, parents of Deaf children, and the community-at-large. You may cancel your subscription at any time. All lessons are taught by Deaf experts of ASL.</p>
    <span class="rule-v" style="left:200px"></span><span class="rule-v" style="left:414px"></span>
    <div class="foot-col quick"><h4>Quick Links</h4>Home<br>Try it Free<br>Contact Us</div>
    <div class="foot-col quick2">Group Rate Form<br>Teacher's Guide<br>Gift Certificates<br>FAQs<br>Privacy Policy</div>
    <div class="foot-col contact"><h4>Contact Us</h4><p><svg width="7" height="7"><use href="#pin"/></svg>PO Box 5520, Maple Ridge, MI 48000</p><p><svg width="7" height="7"><use href="#phone"/></svg>(555) 014-2290</p><p><svg width="7" height="7"><use href="#mail"/></svg>info@signquiverly.com</p></div>
    <span class="rule-h"></span>
    <p class="copy">Copyrights © 2021, SignQuiverly. All rights reserved. Terms &amp; Conditions<br>Z: 0.33 sec</p>
    <div class="socials"><span></span><span></span><span></span><span></span><span></span></div>
    <div class="badge-box"></div><div class="x10">x10</div>
  </footer>
</section>

<!-- PAGE 2 -->
<section class="page page--two">
  <header class="site-header">
    <div class="brand-box"><span class="brand-dot"></span><span class="brand-name">SignQuiverly</span></div>
    <div class="header-title">HOW TO LEARN ASL THROUGH VIDEO LESSONS ONLINE</div>
    <div class="header-user">You are currently logged in as &nbsp;Mlarkin</div>
  </header>
  <nav class="main-nav"><span>DASHBOARD</span><span>LESSONS</span><span>LESSONS LIST</span><span>DICTIONARY</span><span>HANDSHAPES</span><span>LOCATIONS</span><span>DICTIONARY</span><span>UPDATE ACCOUNTS</span><span>LOG OUT</span></nav>
  <div class="activity-bar">
    <div class="activity-title"><em>Activity:</em> Choose the Correct Sentence</div>
    <div class="activity-sub">After viewing the video choose the correct word &amp; phrase</div>
    <div class="fav-label">Add to Favorites</div>
    <div class="fav-btn"><b>+</b> / -</div>
  </div>
  <h2 class="section-title">Choose the Correct Sentence</h2>

  <article class="card" style="top:216px"><div class="badge">1</div>
    <ul class="options"><li><span class="box"></span>Blue cars are my favorite</li><li><span class="box"></span>I love yellow cars</li><li><span class="box"></span>Did you see the silver car?</li><li><span class="box"></span>I want a yellow car.</li></ul>
    <div class="answer">Answer: <span>Show</span></div>
    <div class="video video--wide" role="img" aria-label="ASL instructor signing the sentence on a green backdrop"><span class="slow">Slow video playback</span><svg class="play"><use href="#play"/></svg><div class="controls">▶ &nbsp;0:00 / 0:04<em>◀ ⛶ ⋮</em><i></i></div></div>
  </article>
  <article class="card" style="top:413px"><div class="badge">2</div>
    <ul class="options"><li><span class="box"></span>Pink is a nice color.</li><li><span class="box"></span>Purple is a nice color.</li><li><span class="box"></span>Green and white are the best colors.</li><li><span class="box"></span>love the color orange.</li></ul>
    <div class="answer">Answer: <span>Show</span></div>
    <div class="video video--wide" role="img" aria-label="ASL instructor signing the sentence on a green backdrop"><span class="slow">Slow video playback</span><svg class="play"><use href="#play"/></svg><div class="controls">▶ &nbsp;0:00 / 0:04<em>◀ ⛶ ⋮</em><i></i></div></div>
  </article>
  <article class="card" style="top:609px"><div class="badge">3</div>
    <ul class="options"><li><span class="box"></span>I love blue and yellow!</li><li><span class="box"></span>I love scarlet and grey.</li><li><span class="box"></span>I love green and white.</li><li><span class="box"></span>I like blue and yellow!</li></ul>
    <div class="answer">Answer: <span>Show</span></div>
    <div class="video video--wide" role="img" aria-label="ASL instructor signing the sentence on a green backdrop"><span class="slow">Slow video playback</span><svg class="play"><use href="#play"/></svg><div class="controls">▶ &nbsp;0:00 / 0:04<em>◀ ⛶ ⋮</em><i></i></div></div>
  </article>
  <article class="card" style="top:806px"><div class="badge">4</div>
    <ul class="options"><li><span class="box"></span>Blue and yellow make green.</li><li><span class="box"></span>My favorite colors are red and white.</li><li><span class="box"></span>Do you like white and tan.</li><li><span class="box"></span>Her shirt is rad and purple.</li></ul>
    <div class="answer">Answer: <span>Show</span></div>
    <div class="video video--wide" role="img" aria-label="ASL instructor signing the sentence on a green backdrop"><span class="slow">Slow video playback</span><svg class="play"><use href="#play"/></svg><div class="controls">▶ &nbsp;0:00 / 0:04<em>◀ ⛶ ⋮</em><i></i></div></div>
  </article>
  <article class="card" style="top:1003px"><div class="badge">5</div>
    <ul class="options"><li><span class="box"></span>Doyou like the color green?</li><li><span class="box"></span>Do You like orange or yellow?</li><li><span class="box"></span>I don't like the color orange.</li><li><span class="box"></span>Do you like the color orange?</li></ul>
    <div class="answer">Answer: <span>Show</span></div>
    <div class="video video--wide" role="img" aria-label="ASL instructor signing the sentence on a green backdrop"><span class="slow">Slow video playback</span><svg class="play"><use href="#play"/></svg><div class="controls">▶ &nbsp;0:00 / 0:04<em>◀ ⛶ ⋮</em><i></i></div></div>
  </article>

  <div class="submit">I.M' DONE SUBMIT MY ANSWERS</div>

  <footer class="site-footer">
    <div class="foot-brand"><span class="brand-dot"></span><span class="brand-name">SignQuiverly</span></div>
    <p class="foot-about">SignQuiverly is a subscription based website for American Sign Language (ASL) video lessons. The content is for anyone who wishes to learn ASL, regardless of age. It has been designed to instruct Deaf students, parents of Deaf children, and the community-at-large. You may cancel your subscription at any time. All lessons are taught by Deaf experts of ASL.</p>
    <span class="rule-v" style="left:200px"></span><span class="rule-v" style="left:414px"></span>
    <div class="foot-col quick"><h4>Quick Links</h4>Home<br>Try it Free<br>Contact Us</div>
    <div class="foot-col quick2">Group Rate Form<br>Teacher's Guide<br>Gift Certificates<br>FAQs<br>Privacy Policy</div>
    <div class="foot-col contact"><h4>Contact Us</h4><p><svg width="7" height="7"><use href="#pin"/></svg>PO Box 5520, Maple Ridge, MI 48000</p><p><svg width="7" height="7"><use href="#phone"/></svg>(555) 014-2290</p><p><svg width="7" height="7"><use href="#mail"/></svg>info@signquiverly.com</p></div>
    <span class="rule-h"></span>
    <p class="copy">Copyrights © 2021, SignQuiverly. All rights reserved. Terms &amp; Conditions<br>Z: 0.33 sec</p>
    <div class="socials"><span></span><span></span><span></span><span></span><span></span></div>
    <div class="badge-box"></div><div class="x10">x10</div>
  </footer>
</section>

<!-- PAGE 3 -->
<section class="page page--three">
  <header class="site-header">
    <div class="brand-box"><span class="brand-dot"></span><span class="brand-name">SignQuiverly</span></div>
    <div class="header-title">HOW TO LEARN ASL THROUGH VIDEO LESSONS ONLINE</div>
    <div class="header-user">You are currently logged in as &nbsp;Mlarkin</div>
  </header>
  <nav class="main-nav"><span>DASHBOARD</span><span>LESSONS</span><span>LESSONS LIST</span><span>DICTIONARY</span><span>HANDSHAPES</span><span>LOCATIONS</span><span>DICTIONARY</span><span>UPDATE ACCOUNTS</span><span>LOG OUT</span></nav>
  <div class="activity-bar">
    <div class="activity-title"><em>Activity:</em> Dialouge Illustration</div>
    <div class="activity-sub">After viewing the video choose the correct word &amp; phrase</div>
    <div class="fav-label">Add to Favorites</div>
    <div class="fav-btn"><b>+</b> / -</div>
  </div>
  <h2 class="section-title">Choose the Correct Sentence</h2>

  <article class="card" style="top:216px"><div class="badge">1</div>
    <div class="video video--half video--a" role="img" aria-label="First signer's part of the dialogue on a green backdrop"><span class="slow">Slow video playback</span><svg class="play"><use href="#play"/></svg><div class="controls">▶ &nbsp;0:00 / 0:04<em>◀ ⛶ ⋮</em><i></i></div></div>
    <div class="video video--half video--b" role="img" aria-label="Second signer's reply on a green backdrop"><svg class="play"><use href="#play"/></svg><div class="controls">▶ &nbsp;0:00 / 0:02<em>◀ ⛶ ⋮</em><i></i></div></div>
    <div class="reviewed"><span class="box"></span>Yes I've reviewed this video</div>
  </article>
  <article class="card" style="top:413px"><div class="badge">2</div>
    <div class="video video--half video--a" role="img" aria-label="First signer's part of the dialogue on a green backdrop"><span class="slow">Slow video playback</span><svg class="play"><use href="#play"/></svg><div class="controls">▶ &nbsp;0:00 / 0:04<em>◀ ⛶ ⋮</em><i></i></div></div>
    <div class="video video--half video--b" role="img" aria-label="Second signer's reply on a green backdrop"><svg class="play"><use href="#play"/></svg><div class="controls">▶ &nbsp;0:00 / 0:02<em>◀ ⛶ ⋮</em><i></i></div></div>
    <div class="reviewed"><span class="box"></span>Yes I've reviewed this video</div>
  </article>
  <article class="card" style="top:609px"><div class="badge">3</div>
    <div class="video video--half video--a" role="img" aria-label="First signer's part of the dialogue on a green backdrop"><span class="slow">Slow video playback</span><svg class="play"><use href="#play"/></svg><div class="controls">▶ &nbsp;0:00 / 0:04<em>◀ ⛶ ⋮</em><i></i></div></div>
    <div class="video video--half video--b" role="img" aria-label="Second signer's reply on a green backdrop"><svg class="play"><use href="#play"/></svg><div class="controls">▶ &nbsp;0:00 / 0:02<em>◀ ⛶ ⋮</em><i></i></div></div>
    <div class="reviewed"><span class="box"></span>Yes I've reviewed this video</div>
  </article>
  <article class="card" style="top:806px"><div class="badge">4</div>
    <div class="video video--half video--a" role="img" aria-label="First signer's part of the dialogue on a green backdrop"><span class="slow">Slow video playback</span><svg class="play"><use href="#play"/></svg><div class="controls">▶ &nbsp;0:00 / 0:04<em>◀ ⛶ ⋮</em><i></i></div></div>
    <div class="video video--half video--b" role="img" aria-label="Second signer's reply on a green backdrop"><svg class="play"><use href="#play"/></svg><div class="controls">▶ &nbsp;0:00 / 0:02<em>◀ ⛶ ⋮</em><i></i></div></div>
    <div class="reviewed"><span class="box"></span>Yes I've reviewed this video</div>
  </article>
  <article class="card" style="top:1003px"><div class="badge">5</div>
    <div class="video video--half video--a" role="img" aria-label="First signer's part of the dialogue on a green backdrop"><span class="slow">Slow video playback</span><svg class="play"><use href="#play"/></svg><div class="controls">▶ &nbsp;0:00 / 0:04<em>◀ ⛶ ⋮</em><i></i></div></div>
    <div class="video video--half video--b" role="img" aria-label="Second signer's reply on a green backdrop"><svg class="play"><use href="#play"/></svg><div class="controls">▶ &nbsp;0:00 / 0:02<em>◀ ⛶ ⋮</em><i></i></div></div>
    <div class="reviewed"><span class="box"></span>Yes I've reviewed this video</div>
  </article>

  <div class="submit">I.M' DONE SUBMIT MY ANSWERS</div>

  <footer class="site-footer">
    <div class="foot-brand"><span class="brand-dot"></span><span class="brand-name">SignQuiverly</span></div>
    <p class="foot-about">SignQuiverly is a subscription based website for American Sign Language (ASL) video lessons. The content is for anyone who wishes to learn ASL, regardless of age. It has been designed to instruct Deaf students, parents of Deaf children, and the community-at-large. You may cancel your subscription at any time. All lessons are taught by Deaf experts of ASL.</p>
    <span class="rule-v" style="left:200px"></span><span class="rule-v" style="left:414px"></span>
    <div class="foot-col quick"><h4>Quick Links</h4>Home<br>Try it Free<br>Contact Us</div>
    <div class="foot-col quick2">Group Rate Form<br>Teacher's Guide<br>Gift Certificates<br>FAQs<br>Privacy Policy</div>
    <div class="foot-col contact"><h4>Contact Us</h4><p><svg width="7" height="7"><use href="#pin"/></svg>PO Box 5520, Maple Ridge, MI 48000</p><p><svg width="7" height="7"><use href="#phone"/></svg>(555) 014-2290</p><p><svg width="7" height="7"><use href="#mail"/></svg>info@signquiverly.com</p></div>
    <span class="rule-h"></span>
    <p class="copy">Copyrights © 2021, SignQuiverly. All rights reserved. Terms &amp; Conditions<br>Z: 0.33 sec</p>
    <div class="socials"><span></span><span></span><span></span><span></span><span></span></div>
    <div class="badge-box"></div><div class="x10">x10</div>
  </footer>
</section>

</body>
</html>
```